Professional looking website for solo practitioner law practice

I have recently started up my new law practice. Currently there is just myself practicing here. I would like to have a website that provides my contact information, a map, and the different areas of law that I practice in, being Family Litigation, Wills & Estates, Corporate/Commerical, and Real Estate. I recently had a logo designed so I would like the colours of my website to be congruent with that and include the logo.
I am located in Edmonton, Alberta.

Reason: I will be away for the next few days.

Target Market(s)

individuals and families with an income of $50K+, mostly those looking for family lawyer re divorce, child support, custody and parenting, spousal support.

Industry/Entity Type

Lawyer

Number of Pages Required

4 page

Font styles to use
Serif

Colors
0355a3

Requirements
Must have
• Contact information, ability to email me, background picture(s) that are professional and fit with the legal services theme/service provided but are not single individual lawyers, gavels, or court houses. Need to have click to change the text to include information on Family Litigation, Wills & Estates, Corporate/Commercial, and Real Estate
Nice to have
• contact box
Should not have
• blog, sans serif text, testimonials, news

```html
<!DOCTYPE html>
<html lang="en">
<head>
<meta charset="utf-8">
<title>Marlow Hart Law Office</title>
<link rel="stylesheet" href="https://fonts.googleapis.com/css2?family=Tinos:wght@400;700&family=Open+Sans:wght@400;600&display=swap">
<style>
:root{
  --brand:#0355a3;
  --brand-dark:#0a4a8f;
  --ink:#222;
  --muted:#555;
  --grey:#8a8a8a;
  --line:#d9d9d9;
  --field:#ececec;
  --green:#1cc36f;
  --footer:#333538;
  --white:#fff;
}
*{box-sizing:border-box;margin:0;padding:0}
html,body{width:1200px;height:2161px;overflow:hidden;background:var(--white)}
body{position:relative;font-family:"Tinos",serif;color:var(--ink)}
.abs{position:absolute}

/* header */
.site-header{left:0;top:0;width:1200px;height:136px;background:var(--white)}
.header-divider{top:0;width:1px;height:136px;background:var(--line)}
.header-info{font-family:"Tinos",serif;font-weight:700;font-size:15px;line-height:19px;color:var(--grey)}
.brand{left:426px;top:18px;width:350px;text-align:center}
.brand-mark{width:52px;height:52px;border:3px solid var(--brand);margin:0 auto 8px}
.brand-name{font-size:24px;letter-spacing:1px;color:var(--brand);line-height:24px}
.brand-sub{font-size:12px;letter-spacing:4px;color:var(--brand);line-height:14px}

/* nav */
.main-nav{left:0;top:136px;width:1200px;height:55px;background:var(--brand);display:flex;justify-content:center}
.main-nav a{color:var(--white);text-decoration:none;font-weight:700;font-size:17px;line-height:55px;padding:0 35px;border-right:1px solid rgba(255,255,255,.35)}
.main-nav a:last-child{border-right:none}

/* hero */
.hero{left:0;top:191px;width:1200px;height:649px;background:linear-gradient(100deg,#5c534c 0%,#3a3e48 35%,#6d7481 65%,#a9afb8 100%)}
.hero-title{left:132px;top:338px;font-size:46px;color:var(--white);font-weight:400}
.hero-text{left:132px;top:418px;width:400px;font-size:16px;font-weight:700;line-height:20px;color:var(--white)}
.hero-btn{left:133px;top:522px;width:162px;height:62px;border:2px solid var(--white);color:var(--white);font-weight:700;font-size:16px;line-height:58px;text-align:center}

/* enquiry form */
.form-tab{left:120px;top:748px;width:258px;height:52px;background:#8d8d8d;color:var(--white);font-size:21px;line-height:52px;padding-left:20px}
.enquiry{left:120px;top:800px;width:966px;height:215px;background:var(--brand)}
.field{background:var(--field);font-family:"Open Sans",sans-serif;font-size:14px;color:#444;padding-left:40px;line-height:44px;border-right:1px solid #c9c9c9}
.field-row{left:32px;top:24px;width:902px;height:46px;display:flex}
.message{left:32px;top:74px;width:902px;height:70px;line-height:40px;border:none}
.submit{left:714px;top:150px;width:220px;height:44px;background:var(--green);color:var(--white);font-weight:700;font-size:14px;text-align:center;line-height:44px}

/* services */
.services-head{left:120px;top:1060px;width:1040px;height:60px;display:flex;align-items:center;gap:12px}
.services-head span{flex:1;height:1px;background:var(--brand)}
.services-head h2{font-size:46px;font-weight:400;color:var(--brand)}
.service{top:1160px;width:278px;text-align:center}
.service-photo{width:278px;height:255px;border:6px solid #eee}
.service-icon{position:absolute;left:81px;top:194px;width:116px;height:116px;border-radius:50%;background:var(--brand);border:4px solid var(--white);display:flex;align-items:center;justify-content:center}
.service h3{margin-top:78px;font-size:18px;font-weight:400}
.service p{margin:12px auto 0;width:220px;font-family:"Open Sans",sans-serif;font-size:12px;line-height:17px;color:var(--muted)}
.more{display:inline-block;margin-top:20px;width:112px;height:34px;border:1.5px solid var(--brand-dark);font-family:"Open Sans",sans-serif;font-size:11px;line-height:31px;color:#222}

/* contact */
.map{left:0;top:1722px;width:601px;height:350px;background:linear-gradient(135deg,#7ea9dc 0%,#a9c4e4 40%,#c9d3df 70%,#93b6e0 100%)}
.contact{left:601px;top:1722px;width:599px;height:350px;background:var(--brand);color:var(--white)}
.contact h2{position:absolute;left:90px;top:70px;font-size:33px;font-weight:400}
.contact-item{position:absolute;left:90px;display:flex;align-items:center;gap:40px;font-family:"Open Sans",sans-serif;font-weight:600;font-size:15px;line-height:19px}
.contact-item svg{flex:none}

/* footer */
.site-footer{left:0;top:2072px;width:1200px;height:89px;background:var(--footer)}
.footer-brand{left:130px;top:18px;color:var(--brand);font-size:15px;line-height:16px;display:flex;align-items:center;gap:8px}
.footer-brand i{width:26px;height:26px;border:2px solid var(--brand)}
.footer-nav{left:354px;top:0;display:flex;gap:33px}
.footer-nav a{color:var(--white);text-decoration:none;font-size:14px;font-weight:700;line-height:89px}
.to-top{left:1025px;top:27px}
</style>
</head>
<body>

<header class="site-header abs">
  <svg class="abs" style="left:130px;top:58px" width="26" height="38" viewBox="0 0 26 38"><path d="M13 2C6.9 2 2 6.9 2 13c0 8 11 22 11 22s11-14 11-22C24 6.9 19.1 2 13 2z" fill="none" stroke="#9a9a9a" stroke-width="2"/><circle cx="13" cy="13" r="4" fill="none" stroke="#9a9a9a" stroke-width="2"/></svg>
  <p class="header-info abs" style="left:174px;top:58px">2 Lorum Ipsum, Kansus,<br>Zip code</p>
  <div class="header-divider abs" style="left:424px"></div>
  <div class="brand abs">
    <div class="brand-mark"></div>
    <div class="brand-name">MARLOW HART</div>
    <div class="brand-sub">LAW OFFICE</div>
  </div>
  <div class="header-divider abs" style="left:777px"></div>
  <svg class="abs" style="left:830px;top:58px" width="28" height="42" viewBox="0 0 28 42"><rect x="8" y="2" width="12" height="24" rx="6" fill="#9a9a9a"/><path d="M3 18c0 7 5 12 11 12s11-5 11-12" fill="none" stroke="#9a9a9a" stroke-width="2.5"/><rect x="12.5" y="30" width="3" height="8" fill="#9a9a9a"/></svg>
  <p class="header-info abs" style="left:885px;top:58px">01234-555-010<br>info@marlowhart-law.com</p>
</header>

<nav class="main-nav abs">
  <a href="#">Home</a><a href="#">Family Litigation</a><a href="#">Wills &amp; Estates</a><a href="#">Corporate/Commercial</a><a href="#">Real Estate</a>
</nav>

<section class="hero abs" role="img" aria-label="Photo of a smiling group of professionals in business attire in front of law book shelves"></section>
<h1 class="hero-title abs">Marlow Hart, Attorney</h1>
<p class="hero-text abs">Lorem ipsum dolor sit amet, consectetur adipiscing elit. Nullam pretium urna quis consectetur pulvinar. Nam venenatis rutrum risus sed auctor.</p>
<div class="hero-btn abs">Read More</div>

<div class="form-tab abs">Need legal assistance?</div>
<form class="enquiry abs">
  <div class="field-row abs">
    <div class="field" style="width:235px">Name*</div>
    <div class="field" style="width:220px">Email*</div>
    <div class="field" style="width:226px">Phone*</div>
    <div class="field" style="width:221px;border-right:none">City*</div>
  </div>
  <div class="field message abs">Message*</div>
  <div class="submit abs">SUBMIT NOW</div>
</form>

<div class="services-head abs"><span></span><h2>Services</h2><span></span></div>

<article class="service abs" style="left:31px">
  <div class="service-photo" role="img" aria-label="Photo of a lawyer meeting a young family" style="background:linear-gradient(135deg,#c9b9a6,#8c7c70 60%,#d8cfc4)"></div>
  <div class="service-icon"><svg width="64" height="40" viewBox="0 0 64 40" fill="#fff"><circle cx="32" cy="10" r="8"/><path d="M18 38c0-9 6-15 14-15s14 6 14 15z"/><circle cx="12" cy="14" r="6"/><path d="M0 36c0-7 5-11 12-11 3 0 5 1 7 2-3 3-4 6-4 9z"/><circle cx="52" cy="14" r="6"/><path d="M64 36c0-7-5-11-12-11-3 0-5 1-7 2 3 3 4 6 4 9z"/></svg></div>
  <h3>Family Litigation</h3>
  <p>Lorem ipsum dolor sit amet, consectetur adipiscing elit. Morbi dictum malesuada ipsum ac aliquet.</p>
  <span class="more">MORE INFO</span>
</article>

<article class="service abs" style="left:318px">
  <div class="service-photo" role="img" aria-label="Photo of an estate planning document with a fountain pen" style="background:linear-gradient(160deg,#2b3a55 0%,#e9e3d6 30%,#f3efe6 70%,#d2c7b4)"></div>
  <div class="service-icon"><svg width="40" height="50" viewBox="0 0 40 50"><path d="M3 3h24l10 10v34H3z" fill="none" stroke="#fff" stroke-width="3"/><path d="M10 18h20M10 25h20M10 32h20M10 39h14" stroke="#fff" stroke-width="3"/></svg></div>
  <h3>Wills &amp; Estates</h3>
  <p>Lorem ipsum dolor sit amet, consectetur adipiscing elit. Morbi dictum malesuada ipsum ac aliquet.</p>
  <span class="more">MORE INFO</span>
</article>

<article class="service abs" style="left:605px">
  <div class="service-photo" role="img" aria-label="Photo of a businessman walking between stone columns" style="background:linear-gradient(90deg,#5d6670,#9aa3ad 50%,#4e5761)"></div>
  <div class="service-icon"><svg width="58" height="46" viewBox="0 0 58 46" fill="#fff"><path d="M20 8V3h18v5h-3V6H23v2z"/><rect x="2" y="9" width="54" height="35" rx="3"/><rect x="2" y="24" width="54" height="2" fill="#0355a3"/><rect x="25" y="21" width="8" height="8" fill="#0355a3"/></svg></div>
  <h3>Corporate / Commercial</h3>
  <p>Lorem ipsum dolor sit amet, consectetur adipiscing elit. Morbi dictum malesuada ipsum ac aliquet.</p>
  <span class="more">MORE INFO</span>
</article>

<article class="service abs" style="left:893px">
  <div class="service-photo" role="img" aria-label="Photo of a hand holding house keys in front of a home" style="background:linear-gradient(135deg,#e8dcd6,#c9a696 50%,#dde2e8)"></div>
  <div class="service-icon"><svg width="52" height="48" viewBox="0 0 52 48" fill="#fff"><path d="M26 2 1 24h7v22h13V32h10v14h13V24h7z"/></svg></div>
  <h3>Real Estate</h3>
  <p>Lorem ipsum dolor sit amet, consectetur adipiscing elit. Morbi dictum malesuada ipsum ac aliquet.</p>
  <span class="more">MORE INFO</span>
</article>

<div class="map abs" role="img" aria-label="Street map showing the office location"></div>
<section class="contact abs">
  <h2>How to Contact us</h2>
  <div class="contact-item" style="top:142px"><svg width="20" height="28" viewBox="0 0 20 28"><path d="M10 2C5.6 2 2 5.6 2 10c0 6 8 16 8 16s8-10 8-16c0-4.4-3.6-8-8-8z" fill="none" stroke="#fff" stroke-width="2"/><circle cx="10" cy="10" r="3" fill="none" stroke="#fff" stroke-width="2"/></svg><span>12 LOREUM IPSUM STREET,<br>SOMEWHERE, CITY, ZIP CODE</span></div>
  <div class="contact-item" style="top:196px"><svg width="20" height="30" viewBox="0 0 20 30"><rect x="3" y="2" width="14" height="26" rx="3" fill="none" stroke="#fff" stroke-width="2"/><rect x="7" y="23" width="6" height="2" fill="#fff"/></svg><span>01234-555-010</span></div>
  <div class="contact-item" style="top:250px"><svg width="26" height="20" viewBox="0 0 26 20"><rect x="1" y="1" width="24" height="18" fill="#fff"/><path d="M1 1l12 10L25 1M1 19l9-8M25 19l-9-8" fill="none" stroke="#0355a3" stroke-width="1.5"/></svg><span>info@marlowhart-law.com</span></div>
</section>

<footer class="site-footer abs">
  <div class="footer-brand abs"><i></i><span>MARLOW HART<br>LAW OFFICE</span></div>
  <nav class="footer-nav abs">
    <a href="#">Home</a><a href="#">Family Litigation</a><a href="#">Wills &amp; Estates</a><a href="#">Corporate/Commercial</a><a href="#">Real Estate</a>
  </nav>
  <svg class="to-top abs" width="30" height="34" viewBox="0 0 30 34"><path d="M15 0 30 34 15 24 0 34z" fill="#fff"/></svg>
</footer>

</body>
</html>
```